Business Card & Letterhead Design

We a financial advice company based in Australia. We provide advice to wealthy farmers.

We are changing our business name FROM Brightmere Financial TO Calderstone Wealth and we need a new letterhead and double sided business card design

Attached is designs from our previous branding (Brightmere Financial) as it includes all the details we require on the new Calderstone Wealth business cards and letterhead.

```html
<!DOCTYPE html>
<html lang="en">
<head>
<meta charset="utf-8">
<title>Calderstone Wealth Letterhead</title>
<link href="https://fonts.googleapis.com/css2?family=Cinzel:wght@400&family=Montserrat:ital,wght@0,400;1,400&display=swap" rel="stylesheet">
<style>
  :root {
    --backdrop: #e4e5e7;
    --paper: #ffffff;
    --paper-tone: #f4f4f5;
    --ink: #3d3d3d;
    --ink-soft: #4a4a4a;
    --rule: #8a8a8a;
    --band: #454545;
    --band-text: #ffffff;
  }
  * { margin: 0; padding: 0; box-sizing: border-box; }
  html, body { width: 1200px; height: 1200px; overflow: hidden; background: var(--backdrop); }
  .letterhead {
    position: absolute; left: 233px; top: 93px; width: 735px; height: 1019px;
    background: var(--paper); overflow: hidden;
    font-family: "Montserrat", Arial, sans-serif; color: var(--ink-soft);
  }
  .paper-texture {
    position: absolute; inset: 0;
    background: linear-gradient(180deg, var(--paper-tone) 0%, #fafafa 50%, var(--paper-tone) 100%);
  }
  .brand {
    position: absolute; left: 40px; top: 55px; width: 290px; text-align: center;
  }
  .brand-circle {
    width: 62px; height: 62px; border: 3px solid var(--ink); border-radius: 50%;
    margin: 0 auto 10px;
  }
  .brand-name {
    font-family: "Cinzel", Georgia, serif; font-weight: 400; font-size: 21px;
    letter-spacing: 0.3px; color: var(--ink); white-space: nowrap;
  }
  .contact-list {
    position: absolute; left: 497px; top: 58px; list-style: none;
  }
  .contact-item {
    display: flex; align-items: center; height: 17.6px; font-size: 11px; color: var(--ink-soft);
  }
  .contact-icon { width: 14px; height: 14px; margin-right: 6px; flex: none; }
  .legal {
    position: absolute; left: 0; width: 735px; text-align: center;
    font-size: 10.3px; line-height: 15px; color: var(--ink-soft); white-space: nowrap;
  }
  .legal-entity { top: 866px; }
  .legal-licensee { top: 911px; }
  .legal-rule {
    position: absolute; left: 65px; top: 905px; width: 605px; height: 1px; background: var(--rule);
  }
  .footer-band { position: absolute; left: 0; top: 960px; width: 735px; height: 59px; }
  .footer-tagline {
    position: absolute; left: 0; top: 980px; width: 735px; text-align: center;
    font-style: italic; font-size: 12.5px; line-height: 16px; color: var(--band-text);
  }
</style>
</head>
<body>
  <main class="letterhead">
    <div class="paper-texture" role="img" aria-label="Faint geometric cube pattern across the letterhead background"></div>

    <header class="brand">
      <div class="brand-circle"></div>
      <div class="brand-name">CALDERSTONE WEALTH</div>
    </header>

    <ul class="contact-list">
      <li class="contact-item">
        <svg class="contact-icon" viewBox="0 0 14 14"><circle cx="7" cy="7" r="6.3" fill="none" stroke="#3d3d3d" stroke-width="1"/><path d="M4 6.2c0-1 1.3-1.6 3-1.6s3 .6 3 1.6l-.9.3-.4-.8H5.3l-.4.8zM5 7h4l.6 2.6H4.4z" fill="#3d3d3d"/></svg>
        (07) 3190 4521
      </li>
      <li class="contact-item">
        <svg class="contact-icon" viewBox="0 0 14 14"><circle cx="7" cy="7" r="6.3" fill="none" stroke="#3d3d3d" stroke-width="1"/><rect x="5" y="3.8" width="4" height="2" fill="#3d3d3d"/><rect x="4" y="6.2" width="6" height="3" rx=".5" fill="#3d3d3d"/><rect x="5" y="9.4" width="4" height="1.3" fill="#3d3d3d"/></svg>
        (07) 3190 4522
      </li>
      <li class="contact-item">
        <svg class="contact-icon" viewBox="0 0 14 14"><circle cx="7" cy="7" r="6.3" fill="none" stroke="#3d3d3d" stroke-width="1"/><rect x="5.2" y="3.5" width="3.6" height="7" rx=".6" fill="none" stroke="#3d3d3d" stroke-width="1"/></svg>
        0412 586 730
      </li>
      <li class="contact-item">
        <svg class="contact-icon" viewBox="0 0 14 14"><circle cx="7" cy="7" r="6.3" fill="none" stroke="#3d3d3d" stroke-width="1"/><rect x="3.8" y="4.8" width="6.4" height="4.4" fill="#3d3d3d"/><path d="M3.8 4.8L7 7.4l3.2-2.6" fill="none" stroke="#fff" stroke-width=".7"/></svg>
        tom@calderstonewealth.com.au
      </li>
      <li class="contact-item">
        <svg class="contact-icon" viewBox="0 0 14 14"><circle cx="7" cy="7" r="6.3" fill="none" stroke="#3d3d3d" stroke-width="1"/><circle cx="7" cy="7" r="3.4" fill="none" stroke="#3d3d3d" stroke-width=".8"/><path d="M3.6 7h6.8M7 3.6c-1.4 1.8-1.4 5 0 6.8M7 3.6c1.4 1.8 1.4 5 0 6.8" fill="none" stroke="#3d3d3d" stroke-width=".7"/></svg>
        www.calderstonewealth.com.au
      </li>
    </ul>

    <footer>
      <p class="legal legal-entity">
        Harwick Holdings Pty Ltd - ATF The Ashgrove Investment - Calderstone Wealth<br>
        ABN: 48 302 617 925 - Corporate Authorised - Representative of Summit Advisory Planning Limited
      </p>
      <div class="legal-rule"></div>
      <p class="legal legal-licensee">
        Summit Advisory Planning Limited - ABN: 61 004 318 572<br>
        Australian Financial Services Licence - Licence Number: 318 042<br>
        Principle Address: 215 Harbour St. P.O. Box 4417 Melbourne VIC 3000
      </p>

      <svg class="footer-band" viewBox="0 960 735 59" preserveAspectRatio="none">
        <path d="M0 977 L229 977 L245 1005 L256 965 L485 965 L501 1005 L513 977 L735 977 L735 1019 L0 1019 Z" fill="#454545"/>
      </svg>
      <p class="footer-tagline">A Referral Built Business</p>
    </footer>
  </main>
</body>
</html>
```